BRWN Coaching Website

I would like someone to design my website. I have an existing site which is really basic and needs an overhaul. I have attached a powerpoint with all the information I require. I am flexible with the design and layout and am ok with graphics being added to enhance the attractiveness of the site.

```html
<!DOCTYPE html>
<html lang="en">
<head>
<meta charset="utf-8">
<title>BRWN Coaching</title>
<link href="https://fonts.googleapis.com/css2?family=Nunito:wght@400;600&display=swap" rel="stylesheet">
<style>
:root{
  --blue:#1b74bb;
  --blue-dark:#1565a8;
  --orange:#f05a28;
  --text:#3a3a3a;
  --muted:#555;
  --border:#dfe3e8;
  --white:#fff;
  --footer:#f3f3f3;
  --sky:#e3f0fb;
  --icon:#a7a9ac;
}
*{box-sizing:border-box;margin:0;padding:0}
html,body{width:1200px;height:622px;overflow:hidden}
body{font-family:'Nunito',sans-serif;color:var(--text);position:relative;
  background:linear-gradient(180deg,#dcecfa 42px,#e9f3fc 200px,#f8fbfe 420px,#fbfcfd 508px);}
a{text-decoration:none;color:inherit}
.topbar{position:absolute;left:0;top:0;width:1200px;height:42px;background:var(--blue);color:var(--white);
  font-size:14px;display:flex;align-items:center;justify-content:flex-end;padding-right:130px;gap:10px}
.topbar .item{display:flex;align-items:center;gap:9px}
.topbar .sep{margin:0 4px}
.sky{position:absolute;left:0;top:42px;width:1200px;height:240px;
  background:radial-gradient(ellipse 300px 120px at 80px 180px,rgba(200,226,247,.7),transparent),
  radial-gradient(ellipse 260px 90px at 560px 80px,rgba(200,226,247,.6),transparent),
  radial-gradient(ellipse 220px 110px at 1120px 120px,rgba(200,226,247,.6),transparent)}
.logo{position:absolute;left:130px;top:70px;font-size:26px;font-weight:600;color:var(--blue);display:flex;align-items:center;gap:8px}
.logo .mark{width:14px;height:14px;background:var(--orange)}
.nav{position:absolute;left:433px;top:83px;display:flex;gap:34px;font-size:14px;color:var(--text);letter-spacing:.2px}
.search{position:absolute;left:778px;top:76px;width:205px;height:32px;background:var(--white);border:1px solid #c9ced4;border-radius:2px;box-shadow:inset 0 1px 2px rgba(0,0,0,.12)}
.search svg{position:absolute;right:6px;top:7px}
.btn{background:var(--orange);color:var(--white);font-size:14px;display:flex;align-items:center;justify-content:center;border-radius:2px;letter-spacing:.3px}
.signin{position:absolute;left:998px;top:76px;width:72px;height:32px}
.rule{position:absolute;left:130px;top:142px;width:940px;height:1px;background:var(--white)}
.side-link{position:absolute;left:130px;width:220px;height:52px;background:var(--white);border:1px solid var(--border);
  color:var(--blue);font-size:14px;display:flex;align-items:center;padding-left:18px;letter-spacing:.2px}
.welcome{position:absolute;left:370px;top:158px;width:460px;height:250px;background:var(--white);border:1px solid var(--border);text-align:center;padding:18px 22px}
.welcome h1{font-weight:400;font-size:20px;color:var(--orange);letter-spacing:.3px;margin-bottom:14px}
.welcome p{font-size:13.5px;line-height:20px;color:var(--text)}
.more{display:block;font-size:13.5px;color:var(--blue);margin-top:16px;letter-spacing:.3px}
.cta{position:absolute;left:130px;top:422px;width:700px;height:62px;background:var(--white);border:1px solid var(--border);
  display:flex;align-items:center;padding-left:18px;gap:18px;color:var(--blue);font-size:14px;letter-spacing:.2px}
.cta .btn{width:133px;height:32px}
.bio{position:absolute;left:850px;top:158px;width:220px;height:326px;background:var(--blue);color:var(--white);text-align:center}
.bio h2{height:60px;line-height:62px;font-weight:400;font-size:20px;letter-spacing:.5px}
.bio .photo{height:117px;background:linear-gradient(135deg,#8a8378,#c9b9a6 45%,#6f6a62)}
.bio p{font-size:13.5px;line-height:20px;padding:12px 10px 0}
.bio .more{color:var(--white);margin-top:6px}
.footer{position:absolute;left:0;top:508px;width:1200px;height:114px;background:var(--footer)}
.crumbs{position:absolute;left:130px;top:23px;font-size:11.5px;color:var(--text);letter-spacing:.2px}
.crumbs span{margin:0 6px 0 4px}
.copy{position:absolute;left:130px;top:69px;font-size:11.5px;color:var(--text)}
.copy a{color:var(--blue)}
.follow{position:absolute;left:890px;top:51px;font-size:11.5px;color:var(--blue);letter-spacing:.2px}
.social{position:absolute;top:41px;width:32px;height:32px;border-radius:50%;background:var(--icon)}
</style>
</head>
<body>
<header>
  <div class="topbar">
    <span class="item">
      <svg width="14" height="14" viewBox="0 0 14 14"><rect width="14" height="14" rx="2" fill="#fff"/><path d="M4 3.5c.5-.4 1.2-.3 1.5.3l.6 1.2c.2.4 0 .8-.3 1l-.5.4c.4 1 1.2 1.8 2.2 2.2l.4-.5c.3-.3.7-.4 1-.2l1.2.6c.6.3.7 1 .3 1.5-.7.8-1.8.9-2.8.4C5.6 9.4 4.6 8.4 3.6 6.4c-.5-1-.4-2.2.4-2.9z" fill="#1b74bb"/></svg>
      1300 555 217</span>
    <span class="sep">|</span>
    <span class="item">
      <svg width="17" height="12" viewBox="0 0 17 12"><rect x=".5" y=".5" width="16" height="11" fill="none" stroke="#fff"/><path d="M.5 .5l8 6.5 8-6.5" fill="none" stroke="#fff"/></svg>
      Dana.Marlow@brwncoaching.com</span>
  </div>
  <div class="sky" aria-hidden="true"></div>
  <a class="logo" href="#"><span class="mark"></span>BRWN Coaching</a>
  <nav class="nav"><a href="#">HOME</a><a href="#">BOIGRAPHY</a><a href="#">CONTACT</a></nav>
  <div class="search">
    <svg width="18" height="18" viewBox="0 0 18 18"><circle cx="7" cy="7" r="4.5" fill="none" stroke="#1b74bb" stroke-width="2"/><path d="M10.3 10.3l5 5" stroke="#1b74bb" stroke-width="2.6" stroke-linecap="round"/></svg>
  </div>
  <a class="btn signin" href="#">SIGN IN</a>
  <div class="rule"></div>
</header>
<main>
  <a class="side-link" style="top:158px" href="#">INDIVIDUAL COACHING</a>
  <a class="side-link" style="top:224px" href="#">GROUP WORK</a>
  <a class="side-link" style="top:290px" href="#">RESOURCES</a>
  <a class="side-link" style="top:356px" href="#">INSPIRATION BOOTH</a>
  <section class="welcome">
    <h1>WELCOME TO OUR WEBSITE</h1>
    <p>Welcome to BRWN Coaching where we put a new perspective on the way you work, live and play.</p>
    <p>Through our programs you will learn new skills &amp; techniques to enable you to break through the barriers that have kept you from reaching your full potential up to now.</p>
    <a class="more" href="#">LEARN MORE</a>
  </section>
  <section class="cta">GET YOUR FREE 30 MINUTE INTRODUCTORY COACHING SESSION <a class="btn" href="#">GET STARTED</a></section>
  <aside class="bio">
    <h2>BIOGRAPHY</h2>
    <div class="photo" role="img" aria-label="Portrait photo of coach Dana Marlow outdoors"></div>
    <p>Dana Marlow is a full time working Mum who believes that life is what you make it. She has experience in a variety of industries</p>
    <a class="more" href="#">LEARN MORE</a>
  </aside>
</main>
<footer class="footer">
  <div class="crumbs">HOME<span>/</span> BOIGRAPHY<span>/</span> CONTACT</div>
  <div class="copy">Copyright © 2014. <a href="#">BRWN</a>. All Right Reserved</div>
  <div class="follow">FOLLOW ME ON</div>
  <span class="social" style="left:997px" aria-label="Social link"></span>
  <span class="social" style="left:1039px" aria-label="Social link"></span>
</footer>
</body>
</html>
```